Vostra Capital Web Design

Vostra Capital Limited Shenzhen

This project is a 10 page launch website.
Our client is seeking a contemporary homepage design for a Holdings company. Once we are happy with the homepage design and select designer we will request a secondary page design.

Please see attached company LOGO for an idea of style, it incorporates the traditional Chinese furniture lattice work. The Coral Dune website is one of our clients favorite so we would like to see a similar homepage design to this website.

Use the websites below for reference purpose. The first two are Chinese and the second two are international. We would like to see elements of both but more focus on international design.

http://www.evergrande.com/http://www.orliqueholdings.example/pub/default.aspx http://www.coraldune.example/zh/resort_kelvanoru/
http://www.velde-studio.example
http://img-store-a1.picvault.example/originals/4f/a2/91/4fa291c03b7e55d1a86e20f9c4b713ee.jpg

Company Background
VOSTRA CAPITAL, located in Qianhai, China, is a new real-estate project operator, structuring urban-rural real-estate investment and development, and industrial fund investment. The company also invests in supply chain management and supporting infrastructures. To create new spaces and livable cities Vostra Capital develop win-win strategic partnerships with a number of institutions. Currently cooperating with Marlow East Fenbrook, China urban and rural integrated demonstration.

Target Market(s)

B2B property investment. Target market customers are senior level management/decision makers of large corporations. Focusing geographically on the domestic market first and expanding internationally in 2nd and 3rd years.

Industry/Entity Type

Investment

Requirements
Must have
• Since this is a new company, we would like to the website representing growth and power, E.g. like a growing tree.
Should not have
• Low-level vectors such as curency symbols, American dollar.

```html
<!DOCTYPE html>
<html lang="en">
<head>
<meta charset="utf-8">
<title>Vostra Capital</title>
<link rel="stylesheet" href="https://fonts.googleapis.com/css2?family=Open+Sans:ital,wght@0,300;0,400;0,600;1,400&display=swap">
<style>
:root{
  --gold:#b8922e;
  --gold-light:#cdae5f;
  --gold-dark:#7a5f1c;
  --ink:#555;
  --ink-soft:#777;
  --line:#e6e6e6;
  --panel:#f4f4f4;
  --bar:#2b2b2b;
  --footer:#232323;
  --white:#fff;
}
*{margin:0;padding:0;box-sizing:border-box}
html,body{width:813px;height:1200px;overflow:hidden;background:var(--white)}
body{position:relative;font-family:"Open Sans",Arial,sans-serif;color:var(--ink)}
.abs{position:absolute}

/* header */
.brand{left:110px;top:8px;display:flex;align-items:center;gap:8px}
.brand-mark{width:44px;height:44px;border-radius:50%;border:2px solid var(--gold)}
.brand-name{font-size:14px;font-weight:400;color:var(--gold);letter-spacing:.3px}
.nav{right:110px;top:21px;display:flex;gap:16px;font-size:10.5px;font-weight:300}
.nav a{color:#444;text-decoration:none}
.nav a.active{color:var(--gold)}

.topbar{left:0;top:58px;width:813px;height:23px;background:var(--bar);font-size:6.5px;color:#999}
.lang{left:111px;top:8px}
.lang .on{color:var(--gold)}
.phone{left:385px;top:7px;display:flex;align-items:center;gap:4px}
.search{left:689px;top:4px;width:14px;height:14px;border-radius:50%;background:#666}

/* hero */
.hero{left:0;top:81px;width:813px;height:254px;
  background:linear-gradient(90deg,#5d4a3b 0%,#8a7060 25%,#b9a797 45%,#9e8b7c 65%,#8d6f5a 85%,#6e5847 100%)}
.hero-shade{left:0;top:81px;width:813px;height:254px;background:linear-gradient(180deg,rgba(255,255,255,.08),rgba(60,50,40,.35))}
.hero-title{left:113px;top:160px;font-size:38px;font-weight:400;letter-spacing:23px;color:var(--gold-light)}
.hero-sub{left:112px;top:203px;font-size:41px;font-weight:400;color:var(--white);letter-spacing:.5px}
.cap{left:350px;background:rgba(60,50,45,.75);color:#eee;font-size:7px;padding:3px 5px;line-height:1}
.hero-btn{left:350px;top:230px;width:72px;height:18px;background:var(--white);color:var(--gold);font-size:8px;letter-spacing:1.5px;text-align:center;line-height:18px}
.dot{top:326px;width:16px;height:3px}

/* intro */
.intro{left:0;top:357px;width:813px;text-align:center}
.intro h1{font-size:15.3px;font-weight:300;color:var(--ink)}
.intro p{font-size:10.8px;font-weight:300;margin-top:1px}
.btn-gold{left:360px;top:404px;width:91px;height:20px;background:var(--gold);color:var(--white);font-size:8.5px;letter-spacing:1.6px;text-align:center;line-height:20px}

/* features */
.feature{top:487px;width:190px}
.feature .icon{position:absolute;left:0;top:0;width:24px;height:24px;border-radius:50%;background:var(--gold)}
.feature h3{position:absolute;left:31px;top:2px;font-size:10.5px;font-weight:300;color:var(--ink)}
.feature h3::after{content:"";display:block;width:55px;height:1px;background:var(--line);margin-top:3px}
.feature p{position:absolute;left:31px;top:22px;width:158px;font-size:6.3px;line-height:11px;color:var(--ink-soft)}

/* section titles */
.sec-title{height:12px;display:flex;align-items:center;gap:10px;font-size:11px;font-weight:300;color:var(--gold)}
.sec-title::before,.sec-title::after{content:"";flex:1;height:1px;background:var(--line)}
.arrow{top:589px;width:12px;height:12px;border-radius:50%;background:#ccc}

/* works */
.work{top:604px;width:188px;height:165px;background:var(--panel)}
.work .photo{width:188px;height:116px}
.work h4{position:absolute;left:7px;top:127px;font-size:7.5px;font-weight:400;color:var(--ink)}
.work span{position:absolute;left:7px;top:140px;font-size:5px;color:var(--ink-soft)}

.testimonial{left:515px;top:604px;width:189px;height:144px;background:#f1f1f1}
.testimonial blockquote{position:absolute;left:11px;top:12px;width:168px;font-size:6.8px;line-height:10.7px;font-style:italic;color:var(--ink-soft)}
.testimonial .rule{position:absolute;left:0;top:118px;width:189px;height:1px;background:#ddd}
.testimonial .q{position:absolute;left:84px;top:112px;width:13px;height:13px;border-radius:50%;background:#ccc;color:var(--white);font-size:9px;text-align:center;line-height:14px}
.testimonial cite{position:absolute;left:0;top:128px;width:189px;text-align:center;font-style:normal;font-size:5.5px;color:var(--ink-soft)}
.testimonial cite b{color:var(--ink);font-weight:600}

/* about */
.about-text{left:109px;top:833px;width:194px;font-size:6.4px;line-height:11.2px;color:var(--ink)}
.about-text p+p{margin-top:10px}
.skills{left:515px;top:834px;width:189px}
.skill{height:31.6px;font-size:6px;color:var(--ink)}
.skill .track{margin-top:3px;height:9px;background:var(--panel)}
.skill .fill{height:9px;color:var(--white);font-size:4.5px;text-align:right;padding-right:4px;line-height:9px}

/* footer */
.footer{left:0;top:1012px;width:813px;height:188px;background:var(--footer)}
.f-head{top:1033px;font-size:11px;font-weight:300;color:#ddd}
.addr{left:111px;top:1057px;font-size:6.2px;color:#aaa;line-height:13px}
.addr li{list-style:none;display:flex;gap:6px;align-items:flex-start}
.addr svg{margin-top:3px;flex:none}
.map{left:261px;top:1057px;width:139px;height:91px;border:3px solid var(--white);
  background:linear-gradient(135deg,#e9dfb4,#f1ecd4 40%,#b9c8d6 75%,#e3d7a4)}
.tweet{left:414px;width:137px;height:39px;background:#eee;font-size:6px;color:#888;padding:4px 6px;line-height:10px}
.tweet u{color:#999}
.tweet small{display:block;text-align:right;font-size:5px}
.thumb{width:38px;height:38px;border:1px solid #fff;background:linear-gradient(180deg,#6d6d6d,#3d3a36 60%,#8b8378)}
</style>
</head>
<body>

<!-- header -->
<div class="abs brand"><span class="brand-mark"></span><span class="brand-name">Vostra Capital</span></div>
<nav class="abs nav">
  <a class="active" href="#">Home</a><a href="#">Work</a><a href="#">Blog</a><a href="#">Features</a><a href="#">Services</a><a href="#">Contact</a>
</nav>

<div class="abs topbar">
  <div class="abs lang">Chinese | <span class="on">English</span></div>
  <div class="abs phone">
    <svg width="6" height="6" viewBox="0 0 10 10"><rect x="0" y="0" width="10" height="10" rx="2" fill="#999"/><rect x="3" y="2" width="4" height="6" fill="#2b2b2b"/></svg>
    080-00-000
  </div>
  <div class="abs search">
    <svg width="14" height="14" viewBox="0 0 14 14"><circle cx="6.3" cy="6.3" r="2.6" fill="none" stroke="#fff" stroke-width="1.2"/><line x1="8.2" y1="8.2" x2="10.2" y2="10.2" stroke="#fff" stroke-width="1.3"/></svg>
  </div>
</div>

<!-- hero -->
<div class="abs hero" role="img" aria-label="Blurred city street with buildings and traffic"></div>
<div class="abs hero-shade"></div>
<div class="abs hero-title">TITLE</div>
<div class="abs hero-sub">SUBTITLE</div>
<div class="abs cap" style="top:168px">Lorem ipsum dolor sit amet, consectetur.</div>
<div class="abs cap" style="top:186px">Consectetur adipiscing elit mollis.</div>
<div class="abs cap" style="top:204px">Nulla mollis, neque sed rutrum mollis elit lectus.</div>
<div class="abs hero-btn">GO TO LINK</div>
<div class="abs dot" style="left:381px;background:var(--gold)"></div>
<div class="abs dot" style="left:399px;background:#ccc"></div>

<!-- intro -->
<section class="abs intro">
  <h1>Lorem Ipsum Dolor sit amet, consectetur adipiscing elit. Nullam.</h1>
  <p>Lorem ipsum dolor sit amet, consectetur adipiscing elit. Sed pellentesque.</p>
</section>
<div class="abs btn-gold">GET A QOUTE</div>

<!-- features -->
<div class="abs feature" style="left:109px">
  <span class="icon"><svg width="24" height="24" viewBox="0 0 24 24"><line x1="8" y1="7" x2="8" y2="18" stroke="#fff" stroke-width="1.3"/><path d="M8.6 7.5h8l-2 2.5 2 2.5h-8z" fill="#fff"/></svg></span>
  <h3>Feature One</h3>
  <p>Lorem ipsum dolor sit amet, consectetur adipiscing elit. Nulla mollis, neque sed rutrum mollis, augue leo suscipit lectus, sit amet luctus nisi felis sed justo.</p>
</div>
<div class="abs feature" style="left:312px">
  <span class="icon"><svg width="24" height="24" viewBox="0 0 24 24"><path d="M7 17c0-6 4-9 10-10-1 6-4 10-10 10z" fill="#fff"/></svg></span>
  <h3>Feature Two</h3>
  <p>Lorem ipsum dolor sit amet, consectetur adipiscing elit. Nulla mollis, neque sed rutrum mollis, augue leo suscipit lectus, sit amet luctus nisi felis sed justo.</p>
</div>
<div class="abs feature" style="left:516px">
  <span class="icon"><svg width="24" height="24" viewBox="0 0 24 24"><circle cx="9" cy="9" r="2.3" fill="#fff"/><circle cx="15" cy="9" r="2.3" fill="#fff"/><circle cx="12" cy="13" r="2.3" fill="#fff"/><path d="M8 19a4 3 0 0 1 8 0z" fill="#fff"/></svg></span>
  <h3>Feature Three</h3>
  <p>Lorem ipsum dolor sit amet, consectetur adipiscing elit. Nulla mollis, neque sed rutrum mollis, augue leo suscipit lectus, sit amet luctus nisi felis sed justo.</p>
</div>

<!-- works & testimonials -->
<div class="abs sec-title" style="left:109px;top:577px;width:391px">Our Works</div>
<div class="abs sec-title" style="left:515px;top:577px;width:189px">Testimonials</div>
<div class="abs arrow" style="left:473px"></div>
<div class="abs arrow" style="left:488px"></div>

<article class="abs work" style="left:109px">
  <div class="photo" role="img" aria-label="Three colleagues reviewing documents in an office" style="background:linear-gradient(135deg,#e9f2f4,#7fa8c2 45%,#3d5a72)"></div>
  <h4>Work Title - Lumera</h4><span>DESKTOP</span>
</article>
<article class="abs work" style="left:312px">
  <div class="photo" role="img" aria-label="Businessman laughing on the phone at his desk" style="background:linear-gradient(135deg,#d9e4ea,#8fb0c8 45%,#465e70)"></div>
  <h4>Work Title - Lumera</h4><span>DESKTOP</span>
</article>

<div class="abs testimonial">
  <blockquote>Lorem ipsum dolor sit amet, consectetur adipiscing elit. Vestibulum tincidunt suscipit risus eu porta. Nullam ut gravida leo. Cras tristique nibh sed nunc pharetra vitae condimentum libero sagittis. Nunc ut elit quis nibh pharetra porta in eu leo. Praesent accumsan lobortis neque tempor ornare. Phasellus justo lorem, pharetra ac dictum tempor, sagittis ac risus.</blockquote>
  <div class="rule"></div>
  <div class="q">&ldquo;</div>
  <cite><b>Richard Doe</b> &nbsp;- &nbsp;CEO &nbsp;- &nbsp;Norvex Inc</cite>
</div>
<div class="abs" style="left:676px;top:754px;width:16px;height:2px;background:#ddd"></div>
<div class="abs" style="left:694px;top:754px;width:10px;height:2px;background:var(--gold)"></div>

<!-- about & skills -->
<div class="abs sec-title" style="left:109px;top:806px;width:595px">About &amp; Skills</div>
<div class="abs about-text">
  <p>Lorem ipsum dolor sit amet, consectetur adipiscing elit. Vivamus tempor nulla vel justo congue, in adipiscing tortor pellentesque. Vestibulum ante ipsum primis in faucibus orci luctus et ultrices posuere cubilia Curae; Integer feugiat imperdiet massa nec pulvinar. Nullam vel tortor bibendum, luctus odio at, dictum dui.</p>
  <p>Pellentesque porta tristique tortor, at tincidunt libero lobortis ut. Maecenas nulla erat, feugiat at sollicitudin id, dignissim et nunc. Nullam non commodo dui. Proin suscipit vitae nunc quis congue.</p>
</div>

<svg class="abs" style="left:330px;top:830px" width="150" height="150" viewBox="0 0 150 150" aria-label="Services diagram">
  <g fill="none" stroke="var(--gold)" stroke-width="4">
    <path d="M13 54 A66 66 0 0 1 107 17"/>
    <path d="M126 27 A66 66 0 0 1 127 114"/>
    <path d="M111 129 A66 66 0 0 1 11 85"/>
  </g>
  <g fill="#555" font-family="Open Sans, sans-serif" font-size="10" font-weight="300">
    <text transform="translate(36 47) rotate(-30)">Service 1</text>
    <text transform="translate(118 52) rotate(78)">Service 2</text>
    <text transform="translate(33 98) rotate(33)">Service 3</text>
  </g>
</svg>

<div class="abs skills">
  <div class="skill">Skill 1<div class="track"><div class="fill" style="width:84%;background:var(--gold-light)">80%</div></div></div>
  <div class="skill">Skill 2<div class="track"><div class="fill" style="width:84%;background:#3e3010">85%</div></div></div>
  <div class="skill">Skill 3<div class="track"><div class="fill" style="width:68%;background:#8a6d26">70%</div></div></div>
  <div class="skill">Skill 4<div class="track"><div class="fill" style="width:60%;background:var(--gold-light)">60%</div></div></div>
  <div class="skill">Skill 5<div class="track"><div class="fill" style="width:77%;background:#5e4816">75%</div></div></div>
</div>

<!-- footer -->
<footer class="abs footer"></footer>
<div class="abs f-head" style="left:109px">Address</div>
<div class="abs f-head" style="left:261px">Our Location</div>
<div class="abs f-head" style="left:414px">Latest Tweets</div>
<div class="abs f-head" style="left:566px">Latest Gallery Photos</div>

<ul class="abs addr">
  <li><svg width="6" height="8" viewBox="0 0 6 8"><path d="M3 0a3 3 0 0 1 3 3c0 2-3 5-3 5S0 5 0 3a3 3 0 0 1 3-3z" fill="#ddd"/></svg><span>Building No, Street Name,<br>City, Postal code &nbsp;Country</span></li>
  <li><svg width="6" height="6" viewBox="0 0 6 6"><path d="M1 0l1.5 1.5-.7 1a4 4 0 0 0 1.7 1.7l1-.7L6 5 5 6C2 6 0 4 0 1z" fill="#ddd"/></svg><span>+61 (0) 3 5550 1234</span></li>
  <li><svg width="6" height="6" viewBox="0 0 6 6"><path d="M1 0l1.5 1.5-.7 1a4 4 0 0 0 1.7 1.7l1-.7L6 5 5 6C2 6 0 4 0 1z" fill="#ddd"/></svg><span>+61 (0) 3 5550 1234</span></li>
  <li><svg width="7" height="6" viewBox="0 0 7 6"><rect x=".5" y=".5" width="6" height="5" fill="none" stroke="#ddd"/><path d="M.5 .5l3 2.5 3-2.5" fill="none" stroke="#ddd"/></svg><span>info@vostra.example</span></li>
  <li><svg width="6" height="6" viewBox="0 0 6 6"><circle cx="3" cy="3" r="3" fill="#ddd"/></svg><span>www.vostra.example</span></li>
</ul>

<div class="abs map" role="img" aria-label="Street map showing the office location"></div>

<div class="abs tweet" style="top:1057px"><u>@vostraCapital</u> I'll let Support know now. Thanks! ^TK<small>about 3 hours ago</small></div>
<div class="abs tweet" style="top:1104px"><u>@vostraCapital</u> I'll let Support know now. Thanks! ^TK<small>about 3 hours ago</small></div>

<div class="abs thumb" style="left:566px;top:1058px" role="img" aria-label="Team group photo"></div>
<div class="abs thumb" style="left:611px;top:1058px" role="img" aria-label="Team group photo"></div>
<div class="abs thumb" style="left:655px;top:1058px" role="img" aria-label="Team group photo"></div>
<div class="abs thumb" style="left:566px;top:1104px" role="img" aria-label="Team group photo"></div>
<div class="abs thumb" style="left:611px;top:1104px" role="img" aria-label="Team group photo"></div>
<div class="abs thumb" style="left:655px;top:1104px" role="img" aria-label="Team group photo"></div>

</body>
</html>
```